Business Card for Start Up Real Estate Company

We need a business card designed for a new real estate company called Belvanta. We plan on improving the experience of real estate transactions for both consumers and agents by using current and evolving technology. We would like to see designs that use our existing logo (attached). Please use a primarily white or light colored background. The final design should communicate technology, sophistication and customer service. Thank you...

Industry/Entity Type

Real Estate

Requirements
Must have
• Primarily white or light colored background
Nice to have
• Isolated A from our logo used as part of the design
Should not have
• Pictures, especially of houses

```html
<!DOCTYPE html>
<html lang="en">
<head>
<meta charset="utf-8">
<title>Belvanta Business Card</title>
<link href="https://fonts.googleapis.com/css2?family=Didact+Gothic&family=Tinos&display=swap" rel="stylesheet">
<style>
  :root{
    --page:#e9eaec;
    --card:#f6f6f6;
    --brand-blue:#1d5a98;
    --brand-blue-deep:#174c83;
    --accent-red:#e23546;
    --ink:#4a4a4a;
    --rule:#9a9a9a;
  }
  *{box-sizing:border-box;margin:0;padding:0}
  html,body{width:1200px;height:900px;overflow:hidden}
  body{background:var(--page);position:relative;font-family:"Didact Gothic",sans-serif}

  .card{position:absolute;width:560px;height:320px;border-radius:4px;overflow:hidden;
        box-shadow:0 6px 18px rgba(0,0,0,.12)}

  /* back side */
  .card--back{left:320px;top:90px;
    background:linear-gradient(120deg,var(--brand-blue) 0%,var(--brand-blue-deep) 100%)}
  .card--back .back-glow{position:absolute;inset:0}
  .card--back .wordmark{position:absolute;left:0;right:0;top:50%;transform:translateY(-50%);
    text-align:center;color:#fff;font-size:60px;letter-spacing:3px}

  /* front side */
  .card--front{left:320px;top:470px;background:var(--card)}
  .holder{position:absolute;left:40px;top:40px}
  .holder-name{font-family:"Tinos",serif;font-size:19px;color:var(--ink)}
  .holder-role{font-size:15px;color:var(--accent-red);margin-top:2px}
  .card--front .wordmark{position:absolute;right:40px;top:70px;color:var(--brand-blue);
    font-size:44px;line-height:52px;letter-spacing:2px}
  .holder-rule{position:absolute;left:40px;top:140px;width:450px;height:1px;background:var(--rule)}
  .contact{position:absolute;right:36px;top:158px;list-style:none;text-align:right;
    font-size:14px;color:var(--ink);line-height:22px}
  .contact li{display:flex;justify-content:flex-end;align-items:center;gap:12px}
  .contact svg{width:12px;height:12px;fill:var(--accent-red)}
  .edge-bands{position:absolute;left:0;bottom:0;width:560px;height:26px}
</style>
</head>
<body>

<section class="card card--back" aria-label="Card back">
  <svg class="back-glow" viewBox="0 0 560 320" preserveAspectRatio="none" aria-hidden="true">
    <path d="M0 250 Q280 120 560 40 L560 0 L0 0 Z" fill="#fff" opacity=".05"/>
  </svg>
  <div class="wordmark">BELVANTA</div>
</section>

<section class="card card--front" aria-label="Card front">
  <div class="holder">
    <p class="holder-name">Daniel R. Whitmore</p>
    <p class="holder-role">Instructor</p>
  </div>
  <div class="wordmark">BELVANTA</div>
  <div class="holder-rule"></div>

  <ul class="contact">
    <li>555-014-2871
      <svg viewBox="0 0 12 12" aria-hidden="true"><path d="M2.5 1 L4.5 1 L5.3 3.4 L4 4.4 Q5 6.8 7.6 8 L8.6 6.7 L11 7.5 L11 9.5 Q10.8 11 9.3 11 Q1 10.5 1 2.7 Q1 1.2 2.5 1Z"/></svg></li>
    <li>555-014-2874 (fax)
      <svg viewBox="0 0 12 12" aria-hidden="true"><rect x="1" y="5" width="10" height="6" rx="1"/><rect x="3" y="1" width="6" height="4"/></svg></li>
    <li>daniel@belvanta.com
      <svg viewBox="0 0 12 12" aria-hidden="true"><path d="M1 2.5 H11 V9.5 H1 Z M1.5 3 L6 6.5 L10.5 3" stroke="#fff" stroke-width=".8"/></svg></li>
    <li>www.BelvantaHomes.com
      <svg viewBox="0 0 12 12" aria-hidden="true"><circle cx="6" cy="6" r="5"/><path d="M1 6 H11 M6 1 V11" stroke="#fff" stroke-width=".8"/></svg></li>
  </ul>

  <svg class="edge-bands" viewBox="0 0 560 26" preserveAspectRatio="none" aria-hidden="true">
    <polygon points="0,14 210,14 232,26 0,26" fill="var(--accent-red)"/>
    <polygon points="200,8 560,8 560,26 222,26" fill="var(--brand-blue)"/>
    <polygon points="196,8 205,8 228,26 219,26" fill="#fff"/>
  </svg>
</section>

</body>
</html>
```